Business Card Design

building company specialistloft conversion,extension ,bathrooms ,kitchens ,painting and decorating all general building work

Industry/Entity Type

Building

Contact Information for Business Card

K&R Home renewal Ltd
tel -07912468305
email-Rmarek07@brickmail.example
web in progres

Font styles to use
Sans Serif

Requirements
Must have
• name of the company
• all contact details
Nice to have
• some of the skills

```html
<!DOCTYPE html>
<html lang="en">
<head>
<meta charset="utf-8">
<title>K&amp;R Home renewal Ltd – Business Card</title>
<link rel="stylesheet" href="https://fonts.googleapis.com/css2?family=Kumbh+Sans:wght@500;600;700&display=swap">
<style>
  :root {
    --paper: #ffffff;
    --trim-line: #1a1a1a;
    --bleed-line: #e05a4a;
    --card-dark: #1f2022;
    --brand-orange: #fd4f00;
    --accent-red: #fa2a0a;
    --text-light: #ffffff;
  }
  html, body {
    margin: 0;
    padding: 0;
    overflow: hidden;
    background: var(--paper);
  }
  .canvas {
    position: relative;
    width: 1200px;
    height: 792px;
    overflow: hidden;
    background: var(--paper);
    font-family: "Kumbh Sans", sans-serif;
  }
  .card-art {
    position: absolute;
    inset: 0;
    width: 1200px;
    height: 792px;
  }
  .company-name {
    position: absolute;
    left: 74px;
    top: 372px;
    margin: 0;
    color: var(--text-light);
    font-size: 32px;
    font-weight: 700;
    white-space: nowrap;
  }
  .person {
    position: absolute;
    right: 128px;
    top: 232px;
    text-align: right;
  }
  .person-name {
    margin: 0;
    color: var(--brand-orange);
    font-size: 60px;
    font-weight: 600;
    line-height: 1;
    letter-spacing: -0.5px;
  }
  .person-role {
    margin: 4px 0 0;
    color: var(--text-light);
    font-size: 25px;
    font-weight: 600;
    line-height: 1;
  }
  .contact-list {
    position: absolute;
    left: 633px;
    top: 558px;
    margin: 0;
    padding: 0;
    list-style: none;
    color: var(--text-light);
    font-size: 27px;
    font-weight: 600;
  }
  .contact-list li {
    height: 52px;
    line-height: 34px;
    white-space: nowrap;
  }
  .contact-web {
    letter-spacing: 1.5px;
  }
</style>
</head>
<body>
<main class="canvas">
  <svg class="card-art" viewBox="0 0 1041 687" preserveAspectRatio="none" aria-hidden="true">
    <rect class="trim-frame" x="2" y="2" width="1037" height="683" fill="none" stroke="var(--trim-line)" stroke-width="1"/>
    <rect class="bleed-frame" x="20" y="20" width="1000" height="645" fill="none" stroke="var(--bleed-line)" stroke-width="0.8"/>
    <rect class="card-face" x="42" y="42" width="956" height="603" fill="var(--card-dark)"/>
    <polygon class="accent-chevron" points="345,42 387,42 557,345 340,645 290,645" fill="var(--accent-red)"/>
    <polygon class="brand-chevron" points="42,42 345,42 557,345 290,645 42,645" fill="var(--brand-orange)"/>
  </svg>

  <h1 class="company-name">K&amp;R Home renewal Ltd</h1>

  <div class="person">
    <p class="person-name">Your Name</p>
    <p class="person-role">President</p>
  </div>

  <ul class="contact-list">
    <li class="contact-phone">07912468305</li>
    <li class="contact-email">Rmarek07@brickmail.example</li>
    <li class="contact-web">www.yourweb@yoursite.example</li>
  </ul>
</main>
</body>
</html>
```